Design our next "BOLD HORIZON" print. Size 12x36 Horizontal.

I am looking for a poster design with the text "Bold Horizon" . The print size will be a 12x36 inches.(Horizontal) It should have the American flag used throughout the design. I am looking for a very proud feeling. Font can be creative but instantly readable. The design can be old world feel and can also use the deep reds and navy blues.The image does not have to be just the flag and text. It can contain other patriotic symbols. Can also have a grungy feel. I have enclosed our last "Bold Horizon " piece for your reference. We are hoping we can get one even better. Thank You.

• Should Not be like the image example I enclosed. It's just a reference. We need something that is new and different. Plain White text.

```html
<!DOCTYPE html>
<html lang="en">
<head>
<meta charset="utf-8">
<title>Bold Horizon – 12x36 Print</title>
<link rel="stylesheet" href="https://fonts.googleapis.com/css2?family=Black+Ops+One&display=swap">
<style>
  :root {
    --paper: #ffffff;
    --flag-white: #f3efe8;
    --flag-red: #c31f2a;
    --flag-navy: #2c3868;
    --band-navy: #2a3464;
    --band-red: #c21e29;
    --star-navy: #1f3550;
    --text-white: #ffffff;
  }
  * { margin: 0; padding: 0; box-sizing: border-box; }
  html, body {
    width: 1200px;
    height: 422px;
    overflow: hidden;
    background: var(--paper);
  }
  .poster {
    position: relative;
    width: 1200px;
    height: 422px;
    background: var(--paper);
  }
  .flag-art {
    position: absolute;
    inset: 0;
    width: 1200px;
    height: 422px;
  }
  .title-band {
    position: absolute;
    left: 544px;
    width: 640px;
    display: flex;
    align-items: center;
    justify-content: center;
    font-family: "Black Ops One", Impact, sans-serif;
    color: var(--text-white);
    letter-spacing: 7px;
    line-height: 1;
  }
  .title-band--top {
    top: 118px;
    height: 74px;
    background: var(--band-navy);
    font-size: 60px;
    padding-right: 10px;
  }
  .title-band--bottom {
    top: 206px;
    height: 80px;
    left: 540px;
    width: 644px;
    background: var(--band-red);
    font-size: 62px;
    box-shadow: 0 6px 8px rgba(0, 0, 0, 0.18);
    padding-right: 12px;
  }
</style>
</head>
<body>
<main class="poster">
  <svg class="flag-art" viewBox="0 0 1200 422" xmlns="http://www.w3.org/2000/svg" aria-hidden="false">
    <defs>
      <clipPath id="flag-field">
        <rect x="16" y="16" width="1168" height="388"/>
      </clipPath>
      <clipPath id="canton-shape">
        <path d="M16 16 H512 L528 160 L448 320 L344 404 H16 Z"/>
      </clipPath>
      <radialGradient id="eagle-tone" cx="0.55" cy="0.45" r="0.6">
        <stop offset="0" stop-color="#5a4a55" stop-opacity="0.55"/>
        <stop offset="0.6" stop-color="#3c4168" stop-opacity="0.35"/>
        <stop offset="1" stop-color="#2c3868" stop-opacity="0"/>
      </radialGradient>
      <path id="star" d="M0 -1 L0.2245 -0.309 L0.951 -0.309 L0.363 0.118 L0.588 0.809 L0 0.382 L-0.588 0.809 L-0.363 0.118 L-0.951 -0.309 L-0.2245 -0.309 Z"/>
    </defs>

    <g class="flag-field" clip-path="url(#flag-field)">
      <rect class="flag-white" x="16" y="16" width="1168" height="388" fill="var(--flag-white)"/>
      <g class="flag-stripes" transform="translate(812 246) rotate(-27)" fill="var(--flag-red)">
        <rect x="-1300" y="-400" width="2600" height="96"/>
        <rect x="-1300" y="-224" width="2600" height="96"/>
        <rect x="-1300" y="-48" width="2600" height="96"/>
        <rect x="-1300" y="128" width="2600" height="96"/>
        <rect x="-1300" y="304" width="2600" height="96"/>
      </g>

      <g class="flag-canton" clip-path="url(#canton-shape)">
        <rect x="16" y="16" width="520" height="388" fill="var(--flag-navy)"/>
        <ellipse class="eagle-emblem" cx="390" cy="250" rx="150" ry="170" fill="url(#eagle-tone)"
                 role="img" aria-label="Faint bald eagle head in profile blended into the star field"/>
        <g class="canton-stars" fill="var(--flag-white)">
          <use href="#star" transform="translate(28 48) scale(34)"/>
          <use href="#star" transform="translate(120 84) scale(34)"/>
          <use href="#star" transform="translate(276 26) scale(34)"/>
          <use href="#star" transform="translate(386 34) scale(34)"/>
          <use href="#star" transform="translate(224 120) scale(34)"/>
          <use href="#star" transform="translate(332 156) scale(34)"/>
          <use href="#star" transform="translate(444 184) scale(34)"/>
          <use href="#star" transform="translate(60 190) scale(34)"/>
          <use href="#star" transform="translate(168 232) scale(34)"/>
          <use href="#star" transform="translate(276 266) scale(34)"/>
          <use href="#star" transform="translate(40 306) scale(34)"/>
          <use href="#star" transform="translate(124 340) scale(34)"/>
        </g>
      </g>
    </g>

    <g class="accent-stars accent-stars--red" fill="var(--flag-red)">
      <use href="#star" transform="translate(600 333) scale(13)"/>
      <use href="#star" transform="translate(652 333) scale(13)"/>
      <use href="#star" transform="translate(704 333) scale(13)"/>
    </g>
    <g class="accent-stars accent-stars--navy" fill="var(--star-navy)">
      <use href="#star" transform="translate(908 333) scale(13)"/>
      <use href="#star" transform="translate(956 333) scale(13)"/>
      <use href="#star" transform="translate(1008 333) scale(13)"/>
    </g>
  </svg>

  <h1 class="title">
    <span class="title-band title-band--top">BOLD</span>
    <span class="title-band title-band--bottom">HORIZON</span>
  </h1>
</main>
</body>
</html>
```